Business Card Design Project

I need a business card designed with these details on the front along with the logo attached on the front.

Address - 517/ 208 Wendlebury st Pellford
Website - www.brackwoodcarvers.com.au
Email - delmar@brackwoodcarvers.com.au
Fax - 1900 417 562
Mobile - 0471390618
Telephone - 1300627059
Licence number - 864207k

```html
<!DOCTYPE html>
<html lang="en">
<head>
<meta charset="utf-8">
<title>Brackwood Carvers – Business Card</title>
<link rel="stylesheet" href="https://fonts.googleapis.com/css2?family=Tinos:wght@700&family=PT+Sans&family=PT+Sans+Narrow&family=Open+Sans&display=swap">
<style>
  :root {
    --page: #ffffff;
    --card: #3b1c15;
    --cream: #f2e2cc;
    --muted: #d8cbbd;
    --tile: #d9c7ae;
    --bullet-light: #e6dccd;
    --bullet-dark: #9c8f7e;
  }
  * { margin: 0; padding: 0; box-sizing: border-box; }
  html, body { width: 1200px; height: 697px; overflow: hidden; background: var(--page); }
  .canvas { position: relative; width: 1200px; height: 697px; }
  .card {
    position: absolute; left: 31px; top: 30px; width: 1131px; height: 637px;
    background: var(--card); overflow: hidden;
  }
  .licence {
    position: absolute; left: 27px; top: 20px; height: 418px;
    writing-mode: vertical-rl; transform: rotate(180deg);
    text-align: right;
    font-family: "Open Sans", sans-serif; font-size: 25px; line-height: 32px; letter-spacing: 2.6px;
    color: var(--muted);
  }
  .brand-square {
    position: absolute; left: 87px; top: 25px; width: 236px; height: 240px;
    background: var(--tile);
  }
  .brand-name {
    position: absolute; left: 374px; top: 25px;
    font-family: "Tinos", "Times New Roman", serif; font-weight: 700;
    font-size: 96px; line-height: 116px; letter-spacing: 1px;
    color: var(--cream); text-transform: uppercase; white-space: nowrap;
  }
  .contact {
    position: absolute; top: 482px; list-style: none;
    line-height: 44px; color: var(--cream);
  }
  .contact li { display: flex; align-items: center; white-space: nowrap; }
  .bullet {
    flex: none; width: 17px; height: 17px;
    background: linear-gradient(135deg, var(--bullet-light), var(--bullet-dark));
  }
  .contact-details {
    left: 35px;
    font-family: "PT Sans", sans-serif; font-size: 32px; letter-spacing: 1.4px;
  }
  .contact-details .bullet { margin-right: 40px; }
  .contact-numbers {
    left: 706px;
    font-family: "PT Sans Narrow", sans-serif; font-size: 36px; letter-spacing: 0.4px;
  }
  .contact-numbers .bullet { margin-right: 47px; }
  .label { width: 147px; }
  .contact-numbers li:last-child .label { width: auto; margin-right: 4px; }
</style>
</head>
<body>
<div class="canvas">
  <section class="card">
    <p class="licence">Licence number: 864207k</p>
    <div class="brand-square"></div>
    <h1 class="brand-name">Brackwood<br>Carvers</h1>
    <ul class="contact contact-details">
      <li><span class="bullet"></span>517/ 208 Wendlebury st Pellford</li>
      <li><span class="bullet"></span>www.brackwoodcarvers.com.au</li>
      <li><span class="bullet"></span>delmar@brackwoodcarvers.com.au</li>
    </ul>
    <ul class="contact contact-numbers">
      <li><span class="bullet"></span><span class="label">Fax:</span>190.041.7562</li>
      <li><span class="bullet"></span><span class="label">Mobile:</span>047.139.0618</li>
      <li><span class="bullet"></span><span class="label">Telephone:</span>130.062.7059</li>
    </ul>
  </section>
</div>
</body>
</html>
```